Web Design for High End Baby Products Gear

We have some work from a designer that just didn't meet standards despite weeks of back and forth. We need someone who can come up with creative colors/fonts/etc. to make the site "pop" and give a clean, inviting feel.

We need three pages designed:

1. Home
2. Category Landing Page
3. Product Detail Page

The current site is www.PramTrailWorks.com

Please DO NOT use current site for inspiration.

The layout should follow pretty close to what we have attached.

We were not even pleased with the logo so for now we are just concentrating on the colors and aesthetic feel of the site. You can use a nice typography type logo. We will probably have the logo done at a later time. Or if you have any ideas please feel free to submit as it may increase chances of winning design. The layout is pretty much done with the product page layout approved by our paid search people.

This is isn't where you need to spend a lot of time with general layout as it is already pretty much complete but you are free to deviate or make suggestions if you think it will help.

Reason: I haven't been able to provide adequate feedback and want to spend appropriate amount of time doing so.

I posted the set of PSD files that the previous designer completed.  We were not happy with the outcome of this.

I said in my brief "Here are a few like companies:

www.wheelnestshop.com
www.cradlelane.com
www.tumbleferntots.com
www.qorvix.com
www.dapplemoss.com
www.ovarenti.com"

What I meant was that these were similar companies to our company with respect to product/customer demographic/etc.

Reason: We have found a few that we really like and are working to determine which designs to continue with.

Thank you for your patience.

Reason: Waiting on feedback from a couple of designers so extending deadline

Thank you all.  We received several designs we really liked.  A couple stood out more than others as they seemed to hit the target on the first go around based on our brief and sample sites submitted.

There are several designers we would like to work with in the future as well as we have about 40 domains we will be developing.

Thank you.

Target Market(s)

Target Market: Female, typically 25-40 yrs old, probably married, probably career minded OR middle to upper middle income (some of our strollers are $500-$1,200), expecting mom or mom, some might have two stroller aged (double strollers). Some of our products are QUALITY (KIV for jogging or running) or QUALITY with STYLE (Fennamor), but the truth is that this is a WANT not a need. Sure people need A stroller but not a $900 Tamsel Stroller. So they have a combination of want and need coupled with ability to pay.

Brand Personality:
Definitely clean, crisp and modern. We want it to “POP” but in color and style. But I guess more directly is we want to be seen as THE or ONE of THE authorities on upper end strollers. Where you can get individual assistance, stroller consultations (yes people call in with their needs and ask advice) and personalized service as opposed to a “big box” type place that tries to be everything to everyone and when you call them you get some guy in a cubicle answering the phone that held his baby niece once. So when someone hits our site or walks into our showroom, they need to know they are in the right place.

Industry/Entity Type

Baby

Requirements
Must have
• Must a clean crisp color scheme, easy to ready, focused on products. Must instill authority, credibility, usability and be simple and uncluttered. Fonts and colors must complement each other to achieve the above.

We need three main images as well for the home page as they will be sliding/rotating images.

Backend is built in Corvane so design must conform to that platform.

We retain exlusive rights to the design and all files
Nice to have
• Please see attached word file for more info.

Here are some sites we like:

www.tinyharbor.com
http://www.cubgrove.com/
http://www.fernlark.com/
http://www.quendatots.com/index.php
http://www.pavrel.com/
http://www.vend-arle.com/
http://www.gorbly.com/
http://www.partycardworkshop.com/

Keep in mind that I may just like only something about the above sites and not everything. It may be color, it may be layout , font color, use of text on home page, but something about them stands out.

Here are a few like companies:

www.wheelnestshop.com
www.cradlelane.com
www.tumbleferntots.com
www.qorvix.com
www.dapplemoss.com
www.ovarenti.com
Should not have
• old dated styles, nothing "frilly"

```html
<!DOCTYPE html>
<html lang="en">
<head>
<meta charset="utf-8">
<title>Pram Trail Works – Home</title>
<link href="https://fonts.googleapis.com/css2?family=Open+Sans:wght@400;600;700&family=Lato:wght@300;400;700&display=swap" rel="stylesheet">
<style>
:root{
  --pink:#e5336a;
  --ink:#222;
  --muted:#7a7a7a;
  --line:#dcdcdc;
  --panel:#f1f1f1;
  --black:#141414;
  --teal:#4fb7c4;
  --backdrop:#f4f4f4;
}
*{box-sizing:border-box;margin:0;padding:0}
html,body{width:1200px;height:900px;overflow:hidden}
body{background:var(--backdrop);font-family:"Open Sans",Arial,sans-serif;color:var(--ink);font-size:9px;position:relative}
.page{position:absolute;left:366px;top:0;width:576px;height:900px;background:#fff;box-shadow:0 0 6px rgba(0,0,0,.12)}
.abs{position:absolute}
a{color:inherit;text-decoration:none}

/* header */
.brand{left:12px;top:26px;display:flex;align-items:center;gap:8px}
.brand-dot{width:38px;height:38px;border-radius:50%;background:var(--pink)}
.brand-name{font-family:"Lato",sans-serif;font-weight:700;font-size:19px;line-height:19px;color:var(--pink);text-transform:uppercase}
.perks{left:238px;top:22px;font-family:"Lato",sans-serif;color:var(--muted);font-size:10px;line-height:12px;text-transform:uppercase}
.perks b{display:block;color:var(--pink);font-size:17px;font-weight:400;line-height:18px}
.account{right:10px;top:22px;font-size:7px;color:var(--muted)}
.phone{right:10px;top:38px;font-family:"Lato",sans-serif;font-size:17px;color:var(--pink);display:flex;align-items:center;gap:6px}
.phone small{display:block;font-size:7px;color:var(--muted);text-align:right}
.search{right:10px;top:70px;display:flex}
.search span{width:112px;height:12px;border:1px solid var(--line)}
.search b{background:var(--pink);color:#fff;font-size:7px;padding:1px 6px}
.nav{left:10px;top:100px;width:556px;height:20px;border-bottom:1px solid var(--line);display:flex;align-items:center;gap:16px;font-size:8px;text-transform:uppercase;color:#555}
.nav .on{color:var(--pink)}
.social{display:flex;gap:4px;margin-left:4px}
.social i{width:12px;height:12px;background:#5a7fc0;display:block}
.social i+i{background:#5bc0e8}
.cart{margin-left:auto;font-size:7px;text-transform:none}
.cart em{color:var(--pink);font-style:normal}

/* sidebar */
.side{left:10px;top:132px;width:122px}
.save{background:var(--pink);color:#fff;padding:8px 8px;height:46px;font-size:7px;line-height:9px}
.save b{font-size:13px;font-family:"Lato",sans-serif}
.brandpick{margin-top:8px;display:flex;align-items:center;gap:6px;padding:3px 6px;border:1px solid var(--line);font-size:6px;color:var(--muted)}
.brandpick b{color:var(--pink);font-size:10px;font-weight:400;display:block}
.brandpick span{flex:1;height:10px;border:1px solid var(--line)}
.box{margin-top:10px;border:1px solid var(--line);background:var(--panel)}
.box h3{background:var(--black);color:#fff;font-weight:400;font-size:7px;padding:6px 8px;text-transform:uppercase}
.box h3 em{color:var(--pink);font-style:normal;font-family:"Lato",sans-serif;font-size:14px;text-transform:none}
.box ul{list-style:none;padding:4px 10px}
.box li{font-size:7px;line-height:15px;color:#666}
.box li.hot{color:var(--pink)}
.box li::before{content:"› ";color:#aaa}
.box .group{font-weight:700;color:#333;font-size:7px;padding:6px 10px 0}
.box .more{color:var(--pink);font-size:7px;padding:0 10px 4px}

/* main */
.hero{left:144px;top:132px;width:422px;height:184px;border:1px solid var(--line);background:#fff}
.hero-copy{left:12px;top:52px}
.hero-copy h1{font-family:"Lato",sans-serif;font-weight:300;color:var(--teal);font-size:34px;line-height:32px;letter-spacing:1px}
.hero-copy h2{font-family:"Lato",sans-serif;font-weight:300;color:var(--teal);font-size:18px;margin-left:28px}
.hero-copy p{font-size:6px;color:var(--muted);width:120px;margin-top:6px;line-height:8px}
.hero-copy b{display:inline-block;margin-top:8px;background:var(--teal);color:#fff;font-size:6px;padding:3px 8px}
.hero-photo{right:0;top:0;width:270px;height:182px;background:linear-gradient(135deg,#eef1ee,#8a8d84 55%,#2a2b27)}
.promos{left:144px;top:330px;width:422px;height:70px;display:flex;gap:4px}
.promo{flex:1;border:1px solid var(--line);position:relative;display:flex}
.promo .shot{width:55%;background:linear-gradient(135deg,#f3d9c6,#d6a98c)}
.promo .txt{flex:1;display:flex;flex-direction:column;justify-content:center;align-items:center;font-family:"Lato",sans-serif;color:var(--pink);font-size:11px;line-height:11px;text-align:center}
.promo .txt small{font-size:6px;color:var(--muted);margin-top:3px}
.strip{left:144px;top:410px;width:422px;height:46px;display:flex;gap:4px}
.news{width:180px;background:var(--panel);border:1px solid var(--line);display:flex;align-items:center;gap:6px;padding:0 6px}
.news .tag{background:var(--teal);color:#fff;font-size:9px;padding:3px 4px;transform:rotate(-12deg)}
.news p{font-size:6px;color:#555;line-height:8px;flex:1}
.news .blog{font-family:"Lato",sans-serif;color:var(--pink);font-size:14px}
.letter{flex:1;background:var(--panel);border:1px solid var(--line);padding:6px 10px}
.letter h4{font-family:"Lato",sans-serif;font-weight:400;color:var(--pink);font-size:11px}
.letter div{display:flex;align-items:center;gap:6px;margin-top:6px}
.letter span{width:110px;height:12px;border:1px solid var(--line);background:#fff}
.letter i{width:14px;height:14px;border-radius:50%;background:var(--pink);color:#fff;font-style:normal;font-size:8px;text-align:center;line-height:14px}
.tab{left:144px;width:422px;height:28px;border-bottom:1px solid var(--line)}
.tab span{display:inline-block;background:var(--panel);border:1px solid var(--line);font-family:"Lato",sans-serif;font-size:11px;padding:6px 10px}
.products{left:144px;top:500px;width:422px;height:120px;display:flex;align-items:center;gap:10px}
.arrow{width:12px;height:12px;border-radius:50%;background:#ddd;color:#777;font-size:8px;text-align:center;line-height:12px}
.card{width:86px;height:120px;border:1px solid var(--line);padding:4px;position:relative;text-align:center}
.card .pic{height:72px;background:linear-gradient(160deg,#f0f0f0,#c9c9c9)}
.card:nth-child(3) .pic{background:linear-gradient(160deg,#fbe3ea,#e47a9b)}
.card:nth-child(4) .pic{background:linear-gradient(160deg,#e8efe8,#5f8a6c)}
.card:nth-child(5) .pic{background:linear-gradient(160deg,#f7e6e6,#c8323a)}
.card h5{font-weight:400;font-size:6px;margin-top:4px}
.card .stars{color:#c0393b;font-size:8px}
.card small{font-size:5.5px;color:var(--muted);display:block}
.price{position:absolute;left:30px;top:50px;width:28px;height:28px;border-radius:50%;background:#d22d2d;color:#fff;font-size:7px;line-height:28px}
.brands{left:144px;top:680px;width:422px;height:40px;display:flex;align-items:center;justify-content:space-between;padding:0 4px;font-weight:700;font-size:11px;color:#333}
.brands .arrow{font-weight:400}

/* footer */
.footer{left:10px;top:750px;width:556px;height:150px;background:var(--black);color:#bbb;padding:12px 16px}
.cols{display:flex;gap:14px}
.col{flex:1;font-size:6.5px;line-height:9px}
.col h6{color:var(--pink);font-size:8px;margin-bottom:3px}
.col div+h6{margin-top:6px}
.copy{position:absolute;left:16px;right:16px;bottom:8px;display:flex;justify-content:space-between;font-size:6.5px;color:#ddd}
.copy span{display:flex;gap:4px;align-items:center}
.copy i{width:9px;height:9px;background:#888;display:block}
</style>
</head>
<body>
<div class="page">
  <header>
    <div class="abs brand"><span class="brand-dot"></span><span class="brand-name">Pram Trail<br>Works</span></div>
    <div class="abs perks">365 Day Returns<b>Free Shipping</b>No Sales Tax<br>Price Match Guarantee</div>
    <div class="abs account">Registry | Check Out | My Account</div>
    <div class="abs phone">
      <svg width="14" height="14" viewBox="0 0 14 14"><rect width="14" height="14" rx="2" fill="#e5336a"/><path d="M4 3l2 2-1 1.5a6 6 0 002.5 2.5L9 8l2 2-1.5 1.5C6 11 3 8 2.5 4.5z" fill="#fff"/></svg>
      <div>1.800.PRAMWAY<small>1-800-772-6929</small></div>
    </div>
    <div class="abs search"><span></span><b>Search</b></div>
    <nav class="abs nav">
      <a class="on">Home</a><a>Sale</a><a>Gift Registry</a><a>Gift Cards</a><a>Contact Us</a><a>Store Location</a><a>Blog</a>
      <span class="social"><i></i><i></i></span>
      <a class="cart">Shopping Cart <em>(3 items)</em></a>
    </nav>
  </header>

  <aside class="abs side">
    <div class="save"><b>Save 5%</b> when you sign up for our newsletter</div>
    <div class="brandpick"><div>Shop by<b>Brand</b></div><span></span></div>
    <div class="box">
      <h3>Shop by <em>Category</em></h3>
      <ul>
        <li class="hot">Baby Strollers (75)</li>
        <li>Child Bike Trailers (24)</li>
        <li>Accessories (36)</li>
        <li>Convertible Kits (18)</li>
        <li>Rain / Sun Covers (22)</li>
        <li>Category 4 (10)</li>
        <li>Category 5 Longer Line for Sample (78)</li>
        <li>Category 6 (4)</li>
      </ul>
    </div>
    <div class="box">
      <h3><em>Refine Results</em></h3>
      <div class="group">Brand</div>
      <ul>
        <li class="hot">Nestora (6)</li>
        <li>KIV (4)</li>
        <li>Infant Carriers (11)</li>
        <li>Tarro (3)</li>
      </ul>
      <div class="more">See All Brands</div>
      <div class="group">Best Use</div>
      <ul>
        <li>Casual (8)</li>
        <li>Cross-training (5)</li>
        <li>Cycling (47)</li>
        <li>Running (5)</li>
      </ul>
    </div>
  </aside>

  <section class="abs hero">
    <div class="abs hero-copy">
      <h1>WALK</h1><h2>YOUR WAY</h2>
      <p>Lorem ipsum is simply dummy text of the printing and typesetting trade.</p>
      <b>READ MORE</b>
    </div>
    <div class="abs hero-photo" role="img" aria-label="Rotating banner photo of a premium stroller outdoors"></div>
  </section>

  <section class="abs promos">
    <div class="promo"><div class="shot" role="img" aria-label="Baby eating solids"></div><div class="txt">STARTING<br>SOLIDS<small>check it out</small></div></div>
    <div class="promo"><div class="shot" role="img" aria-label="Baby close-up"></div><div class="txt">BABY<br>SOLIDS<small>shop now</small></div></div>
    <div class="promo"><div class="shot" role="img" aria-label="Toddler with new arrivals"></div><div class="txt">NEW<br>ARRIVALS<small>see more</small></div></div>
  </section>

  <section class="abs strip">
    <div class="news"><span class="tag">News</span><p>Lorem ipsum is simply dummy text of the printing and typesetting trade.</p><span class="blog">› Blog</span></div>
    <div class="letter"><h4>Sign Up for Our Newsletter</h4><div><span></span><i>›</i></div></div>
  </section>

  <div class="abs tab" style="top:462px"><span>Featured Products</span></div>
  <section class="abs products">
    <span class="arrow">‹</span>
    <div class="card"><div class="pic" role="img" aria-label="Diaper bag product photo"></div><span class="price">$50.00</span><h5>Name Lorem Ipsum</h5><div class="stars">★★★★☆</div><small>(1 Review)</small></div>
    <div class="card"><div class="pic" role="img" aria-label="Pink changing bag product photo"></div><h5>Name Lorem Ipsum</h5><div class="stars">★★★★☆</div><small>(1 Review)</small></div>
    <div class="card"><div class="pic" role="img" aria-label="Striped tote product photo"></div><h5>Name Lorem Ipsum</h5><div class="stars">★★★★☆</div><small>(1 Review)</small></div>
    <div class="card"><div class="pic" role="img" aria-label="Red stroller product photo"></div><h5>Name Lorem Ipsum</h5><div class="stars">★★★★☆</div><small>(1 Review)</small></div>
    <span class="arrow">›</span>
  </section>

  <div class="abs tab" style="top:638px"><span>Featured Brands</span></div>
  <section class="abs brands">
    <span class="arrow">‹</span>
    <span>Nestora</span><span>KIV</span><span>Fennamor</span><span>Tarro</span><span>Lumo</span><span>Vextra</span>
    <span class="arrow">›</span>
  </section>

  <footer class="abs footer">
    <div class="cols">
      <div class="col"><h6>Pram Trail Works</h6>About Us<br>Jobs at PTW<br>100% Satisfaction<br>Guarantee<br>Corporate &amp; Group Sales<br>Privacy Policy<br>Terms of Use<br>Site Rules</div>
      <div class="col"><h6>Become a Seller</h6>Become an PTW Member<br>Member Help<br>Find Membership Number<div></div><h6>More Useful Links</h6>Lorem Ipsum<br>Dolor Sit Amet<br>Tandem Donec</div>
      <div class="col"><h6>Stroller Expert</h6>Stroller Expert Articles<br>Lorem Ipsum Sit<br>Donec Tandem Quisque<div></div><h6>More Useful Links</h6>Lorem Ipsum<br>Dolor Sit Amet<br>Tandem Donec</div>
      <div class="col"><h6>Help</h6>Help Section<br>Contact Us<br>Live Help<br>Order Status<br>Returns &amp; Exchanges<br>Product Safety<br>Shipping Info<br>Another link</div>
    </div>
    <div class="copy"><span>© 2011 Pram Trail Works, All Rights Reserved.</span><span>For The Latest News and Special Offers, Follow Us: <i></i><i></i><i></i><i></i><i></i></span></div>
  </footer>
</div>
</body>
</html>
```